Medical device box for kits used for self testing purposes. Attractive simplistic design

Looking for a design that will go on a box that offer multiple range of medical testing ranging from hormones panel to diabetes and thyroid hormones. looking for something attractive and simple to go on a box 6 x 4.5 x 1 inches. attached are some examples from competitors. and our logo that be incorporated with the design.
Picture of the boxes have been attached, pick the color you think goes best with your design.

Target Market(s)

Patients and regular consumers

Industry/Entity Type

Medical

Requirements
Nice to have
• Simple design that is eye catching

```html
<!DOCTYPE html>
<html lang="en">
<head>
<meta charset="UTF-8">
<title>Vantra Self-Test Kit Box</title>
<link href="https://fonts.googleapis.com/css2?family=Montserrat:wght@800&display=swap" rel="stylesheet">
<style>
  :root {
    --page-bg: #e4e4e6;
    --lid-light: #ffffff;
    --lid-shade: #d9dbde;
    --navy: #0d1640;
    --navy-deep: #08102f;
    --accent-line: #b9c4d6;
    --signal-yellow: #eed21c;
  }
  html, body {
    margin: 0;
    width: 1200px;
    height: 960px;
    overflow: hidden;
    background: var(--page-bg);
  }
  .box-layout {
    position: absolute;
    left: 120px;
    top: 90px;
    width: 960px;
  }
  .lid-top {
    position: relative;
    width: 960px;
    height: 640px;
    background: radial-gradient(ellipse at 45% 35%, var(--lid-light) 0%, #f1f2f4 55%, var(--lid-shade) 100%);
    overflow: hidden;
  }
  .lid-wave {
    position: absolute;
    inset: 0;
    width: 100%;
    height: 100%;
  }
  .brand-name {
    position: absolute;
    left: 0;
    right: 0;
    top: 150px;
    display: flex;
    align-items: center;
    justify-content: center;
    gap: 22px;
    font-family: "Montserrat", sans-serif;
    font-weight: 800;
    font-size: 104px;
    letter-spacing: 4px;
    color: var(--navy);
  }
  .brand-dot {
    width: 64px;
    height: 64px;
    border-radius: 50%;
    background: var(--signal-yellow);
  }
  .health-artwork {
    position: absolute;
    left: 60px;
    top: 420px;
    width: 190px;
    height: 150px;
    border-radius: 28px;
    background: var(--signal-yellow);
  }
  .front-face {
    position: relative;
    width: 960px;
    height: 140px;
    background: linear-gradient(180deg, var(--navy) 0%, var(--navy-deep) 100%);
    display: flex;
    align-items: center;
    justify-content: center;
    gap: 14px;
    font-family: "Montserrat", sans-serif;
    font-weight: 800;
    font-size: 34px;
    letter-spacing: 2px;
    color: var(--signal-yellow);
  }
  .front-dot {
    width: 22px;
    height: 22px;
    border-radius: 50%;
    background: var(--signal-yellow);
  }
</style>
</head>
<body>
  <main class="box-layout">
    <section class="lid-top">
      <svg class="lid-wave" viewBox="0 0 960 640" preserveAspectRatio="none" aria-hidden="true">
        <path d="M0 520 C 260 520, 520 500, 720 400 C 820 350, 900 300, 960 280 L960 640 L0 640 Z" fill="var(--navy)"/>
        <path d="M0 506 C 260 506, 520 486, 720 386 C 820 336, 900 286, 960 266" fill="none" stroke="var(--accent-line)" stroke-width="8"/>
      </svg>
      <div class="brand-name"><span class="brand-dot"></span><span>Vantra</span></div>
      <div class="health-artwork" role="img" aria-label="Yellow heart illustration with a heartbeat line"></div>
    </section>
    <section class="front-face"><span class="front-dot"></span><span>Vantra</span></section>
  </main>
</body>
</html>
```